Dental Design, very professional and noticable

Tindale Ridge Dental Surgery is based in Pelican Waters. We are a fast growing dental surgery and are looking for some professional business cards to send to patients.
We would like to see a design that is Vertical and uses the colours Soft Blue, Silver, White and Black. Maybe a full blue side with moto and details on back? Any other ideas or colours that you may think will make the card look unique is fine.
We need all details on the card that are listed above

Target Market(s)

Families, Retired, Other Professionals and Businesses

Industry/Entity Type

Dental

Contact Information for Business Card

Tindale Ridge Dental Surgery
Family, Cosmetic, Preventative
Dr. Owen Castrey
Dental Surgeon
BDS (Adel) FAE FADI FICD FPFA
phone: (07)50001846
fax: (07)50002917
email: tindaleridgedental@quillpost.com
http://tindaleridgedental.com/

Logo Text

Logo styles of interest
Abstract Logo
Requirements
Must have
• Vertical, Vibrant but Professional, Rounded Edges, Logo on front and back of card (different colours on each side)
Nice to have
• One side completely blue (not sure what shade) with logo and moto on bottom
Other side white, with blue or different coloured logo with details in black and silver?
Logo should show half circle with 1 end as arrow symbolizing pelican waters canal also a magnifine glass also half circled with 1 end as arrow. Any other ideas are welcome.
Should not have
• A tooth. A smile. Toothbrush or Toothpaste. Cornered edges.

```html
<!DOCTYPE html>
<html lang="en">
<head>
<meta charset="utf-8">
<title>Tindale Ridge Dental Surgery – Business Card</title>
<link rel="stylesheet" href="https://fonts.googleapis.com/css2?family=Open+Sans:ital,wght@0,400;0,600;0,700;1,600&family=PT+Serif&display=swap">
<style>
  :root {
    --backdrop: #e8eaed;
    --blue-light: #5089cc;
    --blue-mid: #3d72b8;
    --blue-deep: #2c5c9e;
    --blue-text: #3b73c0;
    --navy: #1f3552;
    --white: #ffffff;
    --black: #111111;
    --silver: #a9adb2;
  }
  * { box-sizing: border-box; margin: 0; padding: 0; }
  html, body { width: 1200px; height: 814px; overflow: hidden; }
  body {
    background: var(--backdrop);
    font-family: "Open Sans", Arial, sans-serif;
    position: relative;
  }
  .card {
    position: absolute;
    top: 57px;
    width: 400px;
    height: 700px;
    border-radius: 26px;
    box-shadow: 0 10px 28px rgba(0,0,0,0.18);
    text-align: center;
  }
  .card--front {
    left: 170px;
    background: radial-gradient(ellipse at 50% 40%, var(--blue-light) 0%, var(--blue-mid) 45%, var(--blue-deep) 100%);
    color: var(--white);
  }
  .card--back {
    left: 630px;
    background: var(--white);
    color: var(--black);
  }
  .mark {
    display: flex;
    align-items: center;
    justify-content: center;
    gap: 14px;
  }
  .mark__dot {
    width: 58px; height: 58px; border-radius: 50%;
  }
  .mark__name {
    font-weight: 600;
    font-size: 22px;
    line-height: 1.15;
    text-align: left;
  }
  .card--front .mark { margin-top: 200px; }
  .card--front .mark__dot { background: var(--white); }
  .card--front .mark__name { color: var(--white); }
  .card--back .mark { margin-top: 70px; }
  .card--back .mark__dot { width: 48px; height: 48px; background: var(--blue-text); }
  .card--back .mark__name { color: var(--blue-text); font-size: 19px; }

  .front__practice {
    margin-top: 62px;
    font-weight: 600;
    font-size: 22px;
  }
  .front__motto {
    margin-top: 14px;
    font-style: italic;
    font-weight: 600;
    font-size: 18px;
    color: var(--navy);
  }

  .back__practice {
    margin-top: 22px;
    font-weight: 600;
    font-size: 18px;
    color: var(--blue-text);
  }
  .back__name {
    margin-top: 20px;
    font-weight: 700;
    font-size: 28px;
    letter-spacing: 0.5px;
  }
  .back__role {
    font-family: "PT Serif", Georgia, serif;
    font-size: 19px;
    letter-spacing: 1px;
    color: var(--silver);
    line-height: 1.1;
  }
  .back__credentials {
    margin-top: 4px;
    font-weight: 700;
    font-size: 13px;
  }
  .back__rule {
    width: 300px;
    height: 2px;
    margin: 22px auto 26px;
    background: var(--blue-text);
    border: 0;
  }
  .contact {
    display: grid;
    grid-template-columns: auto auto;
    justify-content: center;
    column-gap: 14px;
    row-gap: 6px;
    align-items: baseline;
  }
  .contact__label {
    font-family: "PT Serif", Georgia, serif;
    font-size: 16px;
    letter-spacing: 1px;
    color: var(--silver);
    text-align: right;
  }
  .contact__value { font-weight: 700; font-size: 19px; text-align: left; }
  .back__email {
    margin-top: 46px;
    font-weight: 700;
    font-size: 18px;
  }
  .back__web {
    margin-top: 6px;
    font-weight: 600;
    font-size: 19px;
    color: var(--blue-text);
  }
</style>
</head>
<body>
  <section class="card card--front">
    <div class="mark">
      <span class="mark__dot"></span>
      <span class="mark__name">Tindale<br>Ridge</span>
    </div>
    <p class="front__practice">Tindale Ridge Dental Surgery</p>
    <p class="front__motto">Family, Cosmetic, Preventive</p>
  </section>

  <section class="card card--back">
    <div class="mark">
      <span class="mark__dot"></span>
      <span class="mark__name">Tindale Ridge</span>
    </div>
    <p class="back__practice">Tindale Ridge Dental Surgery</p>
    <p class="back__name">Dr. Owen Castrey</p>
    <p class="back__role">DENTAL SURGEON</p>
    <p class="back__credentials">BDS (Adel) FAE FADI FICD FPFA</p>
    <hr class="back__rule">
    <div class="contact">
      <span class="contact__label">PHONE</span><span class="contact__value">(07) 5000 1846</span>
      <span class="contact__label">FAX</span><span class="contact__value">(07) 5000 2917</span>
    </div>
    <p class="back__email">tindaleridgedental@quillpost.com</p>
    <p class="back__web">tindaleridgedental.com</p>
  </section>
</body>
</html>
```